Online business manager needs a website

I need a website designed and then coded. I am an online business manager serving a number of different industries providing administrative support to existing small businesses and helping solo practitioners get their new business up and running.

I didn't have a logo formally designed but have been using the attached avatar and wouldn't mind something that incorporated that.

The business doesn't have an official name, so I've just been using my name Lena Pruvost, Online Business Manager or Lena Pruvost, OBM. I've attached two documents that I have made previously for an example of content.

I would prefer the final site be in Wordpress.

Requirements
Must have
• A way to contact me, testimonials, list of services

```html
<!DOCTYPE html>
<html lang="en">
<head>
<meta charset="utf-8">
<title>Lena Pruvost – Digital Business Manager</title>
<link rel="stylesheet" href="https://fonts.googleapis.com/css2?family=Satisfy&family=Quicksand:wght@400;500;600;700&display=swap">
<style>
:root{
  --space-dark:#0b0a1c;
  --space-mid:#1c1238;
  --purple:#3d1a78;
  --purple-bright:#8a1bb0;
  --coral:#f4544f;
  --ink:#2b2b38;
  --muted:#5a5a68;
  --white:#ffffff;
  --tile:#f4f1f8;
  --star:#f5a623;
}
*{box-sizing:border-box;margin:0;padding:0}
html,body{width:1200px;height:4364px;overflow:hidden}
body{position:relative;background:var(--white);font-family:"Quicksand",sans-serif;color:var(--ink)}
.abs{position:absolute}
.script{font-family:"Satisfy",cursive;font-weight:400}
.space{background:
  radial-gradient(ellipse 380px 260px at 75% 30%,rgba(120,50,140,.55),transparent 70%),
  radial-gradient(ellipse 420px 300px at 20% 70%,rgba(60,40,120,.5),transparent 70%),
  radial-gradient(ellipse 300px 200px at 55% 80%,rgba(150,60,120,.35),transparent 70%),
  linear-gradient(160deg,var(--space-dark),var(--space-mid) 55%,var(--space-dark));}
.btn{position:absolute;background:var(--coral);color:var(--white);border-radius:26px;font-weight:600;font-size:16px;display:flex;align-items:center;justify-content:center;gap:6px}

/* header */
.logo-name{font-size:44px;line-height:1;color:var(--white);white-space:nowrap}
.logo-sub{font-size:24px;color:var(--white);white-space:nowrap}
.nav{left:416px;top:50px;display:flex;gap:48px;color:var(--white);font-weight:600;font-size:16px}

/* hero */
.hero-title{left:612px;top:215px;font-size:68px;line-height:78px;color:var(--white);white-space:nowrap}
.hero-text{left:612px;top:398px;width:500px;font-size:15px;line-height:30px;color:var(--white);font-weight:500}
.slider{left:612px;top:660px;color:var(--white);display:flex;align-items:center;gap:18px;font-weight:600}
.slider .track{width:178px;height:2px;background:rgba(255,255,255,.45);position:relative}
.slider .track i{position:absolute;left:0;top:-1px;width:24px;height:4px;background:var(--coral)}

/* services */
.section-title{left:0;width:1200px;text-align:center;font-size:68px;color:var(--purple)}
.card{top:1076px;width:236px;height:430px}
.card .photo{height:210px;border-radius:32px 32px 0 0}
.card h3{font-family:"Satisfy",cursive;font-weight:400;font-size:23px;line-height:33px;color:var(--purple);margin:14px 0 6px 20px;white-space:nowrap}
.card ul{list-style:none;margin-left:20px;font-size:15px;line-height:29px;color:var(--ink);font-weight:500}
.card .more{position:absolute;top:392px;left:20px;color:var(--coral);font-size:15px;font-weight:600;border-bottom:1px solid var(--coral);padding-bottom:3px}

/* best */
.tile{width:245px;height:195px;border-radius:22px;background:var(--tile);display:flex;flex-direction:column;align-items:center;justify-content:center;gap:14px;color:var(--purple)}
.tile span{font-family:"Satisfy",cursive;font-size:23px;color:#2a1d45;white-space:nowrap}
.tile.active{background:linear-gradient(135deg,var(--purple-bright),#3c1478)}
.tile.active span{color:var(--white)}
.tile svg{width:64px;height:64px;fill:none;stroke:currentColor;stroke-width:2.2;stroke-linejoin:round;stroke-linecap:round}

/* testimonial */
.quote-mark{font-family:"Satisfy",cursive;font-size:140px;line-height:1;color:var(--coral)}
.quote-text{left:200px;top:2780px;width:790px;text-align:center;font-size:20px;line-height:36px;color:#4a4a55}

/* connect */
.contact-item{left:85px;display:flex;align-items:center;gap:18px;color:var(--white);font-weight:600;font-size:20px}
.contact-item svg{width:20px;height:20px;fill:var(--white)}
.field{color:var(--white);font-size:15px;font-weight:500;border-bottom:1px solid rgba(255,255,255,.6);padding-bottom:10px}

/* footer */
.foot-head{font-family:"Satisfy",cursive;font-size:23px;color:var(--purple)}
.foot-list{list-style:none;font-size:15px;line-height:41px;color:var(--ink);font-weight:500}
.foot-list li::before{content:"›";margin-right:12px;color:var(--ink)}
</style>
</head>
<body>

<!-- hero -->
<section class="abs space" style="left:0;top:0;width:1200px;height:820px"></section>
<div class="abs" role="img" aria-label="Portrait photo of the business manager smiling" style="left:0;top:175px;width:620px;height:640px;background:radial-gradient(ellipse 260px 300px at 48% 40%,#c99a6e,#8a6a58 55%,rgba(120,120,130,.9) 80%,transparent 100%);border-radius:40% 40% 0 0"></div>
<svg class="abs" style="left:0;top:600px" width="1200" height="230" viewBox="0 0 1200 230" aria-hidden="true">
  <path d="M0 190 C300 215 620 215 820 170 C980 135 1100 80 1200 20 L1200 230 L0 230Z" fill="#fff"/>
</svg>

<header>
  <div class="abs script logo-name" style="left:85px;top:22px">Lena Pruvost</div>
  <div class="abs script logo-sub" style="left:162px;top:72px">Virtual Assistant</div>
  <nav class="abs nav"><span>Home</span><span>About</span><span>Services</span><span>Blog</span><span>Testimonial</span></nav>
  <div class="btn" style="left:956px;top:37px;width:156px;height:50px">Contact Me</div>
</header>

<h1 class="abs script hero-title">Digital<br>Business Manager</h1>
<p class="abs hero-text">Focused on the live event and entertainment industry. Helping artists and owners to bettermanage their career and business by strategically reviewing systems, recommending operational efficiencies, and managing inboxes</p>
<div class="btn" style="left:612px;top:557px;width:184px;height:50px">Learn More →</div>
<div class="abs slider"><span style="font-size:20px;font-weight:500">01</span><span class="track"><i></i></span><span style="font-size:15px">04</span></div>

<!-- services -->
<h2 class="abs script section-title" style="top:918px">Services</h2>

<article class="abs card" style="left:85px">
  <div class="photo" role="img" aria-label="Laptop on a desk" style="background:linear-gradient(135deg,#d8dde4,#9aa4b0)"></div>
  <h3>Virtual Assistance</h3>
  <ul><li>Calendar Management</li><li>Email Management</li><li>Light Graphic Design</li><li>Data Entry</li></ul>
  <span class="more">View Details →</span>
</article>
<article class="abs card" style="left:349px">
  <div class="photo" role="img" aria-label="Typed motivational note beside a plant" style="background:linear-gradient(135deg,#4f7a3a,#e8e4dc 55%)"></div>
  <h3>Social Media &amp;<br>Content Management</h3>
  <ul><li>Content Repurposing</li><li>Graphics Creation</li><li>Audiogram Creation</li></ul>
  <span class="more">View Details →</span>
</article>
<article class="abs card" style="left:614px">
  <div class="photo" role="img" aria-label="Hands working with a calculator and invoices" style="background:linear-gradient(135deg,#8fd0dc,#e9eef0)"></div>
  <h3>Finance Management</h3>
  <ul><li>Create Invoices</li><li>Track Receivables</li><li>Analyze Expenses</li><li>Year Over Year Analytics</li></ul>
  <span class="more">View Details →</span>
</article>
<article class="abs card" style="left:878px">
  <div class="photo" role="img" aria-label="Two colleagues at laptops in front of a sticky note wall" style="background:linear-gradient(135deg,#e7e2d6,#c9d4c6)"></div>
  <h3>Business Management</h3>
  <ul style="line-height:24px"><li>Creation of Operating<br>Procedures</li><li style="margin-top:6px">Review of Website<br>Strategy</li></ul>
  <span class="more">View Details →</span>
</article>

<!-- what I do best -->
<section class="abs space" style="left:0;top:1610px;width:1200px;height:856px"></section>
<svg class="abs" style="left:0;top:1600px" width="1200" height="220" viewBox="0 0 1200 220" aria-hidden="true">
  <path d="M0 0 L1200 0 L1200 28 C900 20 500 70 0 205Z" fill="#fff"/>
</svg>
<h2 class="abs script section-title" style="top:1795px;color:var(--white);font-size:66px">What I do best</h2>

<div class="abs tile" style="left:85px;top:1930px"><svg viewBox="0 0 64 64"><rect x="14" y="10" width="30" height="42" rx="3"/><path d="M20 22h18M20 30h18M20 38h12M50 14L34 40l-3 6 5-4 16-26z"/></svg><span>Content Repurposing</span></div>
<div class="abs tile active" style="left:346px;top:1930px;color:#fff"><svg viewBox="0 0 64 64"><rect x="16" y="8" width="32" height="44" rx="3"/><path d="M22 18l3 3 5-5M34 19h8M22 28l3 3 5-5M34 29h8M22 38l3 3 5-5M34 39h8M10 56h44"/></svg><span>Data Entry</span></div>
<div class="abs tile" style="left:608px;top:1930px"><svg viewBox="0 0 64 64"><path d="M8 28l24-18 24 18v26H8z"/><path d="M8 28l24 16 24-16"/><circle cx="32" cy="26" r="6"/></svg><span>Email Management</span></div>
<div class="abs tile" style="left:869px;top:1930px"><svg viewBox="0 0 64 64"><rect x="10" y="8" width="30" height="40" rx="3"/><circle cx="25" cy="22" r="6"/><path d="M16 36h18M16 42h12"/><rect x="34" y="30" width="20" height="26" rx="2"/><path d="M38 36h12M39 43h2M45 43h2M39 49h2M45 49h2"/></svg><span>Bookkeeping</span></div>

<div class="abs tile" style="left:85px;top:2162px"><svg viewBox="0 0 64 64"><path d="M10 54h46M16 54V40M26 54V34M36 54V28M46 54V20M14 30l12-8 10 4 16-14M46 12h6v6"/><circle cx="24" cy="46" r="7"/></svg><span>Financial Analytics</span></div>
<div class="abs tile" style="left:346px;top:2162px"><svg viewBox="0 0 64 64"><path d="M32 10l14 22-14 22-14-22z"/><circle cx="32" cy="32" r="4"/><path d="M10 14c10 0 16 4 22-4M54 14c-10 0-16 4-22-4"/><rect x="6" y="10" width="6" height="6"/><rect x="52" y="10" width="6" height="6"/></svg><span>Graphic Creations</span></div>
<div class="abs tile" style="left:608px;top:2162px"><svg viewBox="0 0 64 64"><circle cx="32" cy="26" r="14"/><circle cx="32" cy="26" r="5"/><path d="M26 40v8h12v-8M28 54h8M32 6v4M50 26h4M10 26h4M45 13l3-3M16 10l3 3"/></svg><span>Project Management</span></div>
<div class="abs tile" style="left:869px;top:2162px"><svg viewBox="0 0 64 64"><ellipse cx="32" cy="26" rx="20" ry="12" transform="rotate(-15 32 26)"/><path d="M24 38v14M34 38v14M24 44h10M54 44l3 3M52 52l2-3M10 14l4 2"/></svg><span>More Awesomeness</span></div>

<!-- testimonial -->
<h2 class="abs script section-title" style="top:2572px">Client Love</h2>
<div class="abs quote-mark" style="left:128px;top:2670px">“</div>
<div class="abs" style="left:532px;top:2706px;color:var(--star);font-size:26px;letter-spacing:6px">★★★★★</div>
<p class="abs quote-text">When it became apparent that a project would takemore time than I had, Lena stepped up to take on the required research. She was thorough and timely; able to meet a last-minute 12-hour deadline. I would highly recommend Lena to assist with your next project.</p>
<div class="abs quote-mark" style="left:1005px;top:2858px">”</div>
<div class="abs" style="left:0;width:1200px;top:2950px;text-align:center;font-size:21px;font-weight:600;color:var(--ink)">Dana R.</div>
<div class="abs" style="left:0;width:1200px;top:2984px;text-align:center;font-size:14px;color:var(--muted)">Owner, Brightline Builders</div>

<!-- connect -->
<section class="abs space" style="left:0;top:3125px;width:1200px;height:720px"></section>
<svg class="abs" style="left:0;top:3620px" width="1200" height="240" viewBox="0 0 1200 240" aria-hidden="true">
  <path d="M1200 30 C1000 160 600 230 0 210 L0 240 L1200 240Z" fill="#fff"/>
</svg>
<h2 class="abs script" style="left:85px;top:3240px;font-size:68px;color:var(--white);white-space:nowrap">Let’s Connect</h2>
<div class="abs contact-item" style="top:3378px"><svg viewBox="0 0 24 24"><path d="M12 2a7 7 0 0 0-7 7c0 5 7 13 7 13s7-8 7-13a7 7 0 0 0-7-7zm0 9.5A2.5 2.5 0 1 1 12 6.5a2.5 2.5 0 0 1 0 5z"/></svg>555-014-2290</div>
<div class="abs contact-item" style="top:3441px"><svg viewBox="0 0 24 24"><path d="M2 5h20v14H2z" /><path d="M2 5l10 8 10-8" stroke="#1c1238" stroke-width="2" fill="none"/></svg>hello@lenapruvost-obm.com</div>
<div class="abs contact-item" style="top:3504px"><svg viewBox="0 0 24 24"><rect x="2" y="2" width="20" height="20" rx="2"/></svg>Lena Marie Pruvost</div>

<div class="abs field" style="left:527px;top:3350px;width:275px">First Name</div>
<div class="abs field" style="left:843px;top:3350px;width:271px">Last Name</div>
<div class="abs field" style="left:527px;top:3416px;width:275px">Email</div>
<div class="abs field" style="left:838px;top:3416px;width:276px">Phone No.</div>
<div class="abs field" style="left:527px;top:3480px;width:587px;height:90px">Message</div>
<div class="btn" style="left:930px;top:3597px;width:184px;height:48px">Send Message →</div>

<!-- footer -->
<footer>
  <div class="abs script" style="left:85px;top:3940px;font-size:44px;color:var(--purple);line-height:1;white-space:nowrap">Lena Pruvost</div>
  <div class="abs script" style="left:162px;top:3990px;font-size:24px;color:var(--purple);white-space:nowrap">Virtual Assistant</div>
  <p class="abs" style="left:85px;top:4040px;width:290px;font-size:15px;line-height:26px;color:var(--ink);font-weight:500">Focused on the live event and entertainment industry. Helping artists and owners to better manage their career and business by strategically reviewing systems, recommending operational efficiencies, and managing inboxes</p>

  <div class="abs foot-head" style="left:552px;top:3950px">Quick Links</div>
  <ul class="abs foot-list" style="left:552px;top:3993px"><li>Home</li><li>About</li><li>Services</li><li>Blog</li><li>Testimonial</li><li>Contact</li></ul>

  <div class="abs foot-head" style="left:813px;top:3950px">Services</div>
  <ul class="abs foot-list" style="left:813px;top:3993px"><li>Virtual Assistance</li><li>Social Media &amp; Content Management</li><li>Finance Management</li><li>Business Management</li></ul>

  <div class="abs" style="left:85px;top:4290px;width:1029px;height:1px;background:#d8d8e0"></div>
  <div class="abs" style="left:85px;top:4314px;font-size:14px;color:var(--muted)">© 2023 <span style="color:var(--purple)">Lena Pruvost</span>. All right reserved</div>
  <div class="abs" style="left:900px;width:214px;text-align:right;top:4314px;font-size:14px;color:var(--muted)">July 03, 2023. Layout_4</div>
</footer>

</body>
</html>
```